▼プロジェクト概要 達人ディレクトリに掲載されている専門家が、自社ホームページに掲載するための認定バナーのデザインを募集します。 「第三者機関から認定された信頼できる専門家である」ことを証明し、ブランディング・差別化に活用できるデザインを求めています。 ▼制作の目的 1. 専門家のブランディング強化 第三者機関(達人ディレクトリ)から認定された信頼できる専門家であることを視覚的に証明し、他の専門家との差別化を図る。 2. ユーザーへの安心感提供 ホームページ訪問者に対し、「この専門家は信頼できる」という安心感を与え、問い合わせ率の向上に貢献する。 ▼デザイン仕様 【必須要素】 ・文言: 「達人ディレクトリ掲載専門家」 ・ロゴ::達人ディレクトリの公式ロゴ(添付ファイル参照)【サイズ(3パターン全て制作)】 320px × 100px(スマートフォン向け横長バナー) 300px × 250px(サイドバー向け正方形バナー) 728px × 90px(PC向けヘッダー/フッター用横長バナー) ※全サイズで統一感のあるデザインをお願いします。 ▼デザインの方向性 【求めるイメージ】 ・プロフェッショナル: どのような業種の専門家HPにも馴染むシンプルで洗練されたデザイン ・視認性: 小さいサイズでも文字やロゴがはっきり見える ・汎用性: 士業、コンサルタント、医療、不動産など、様々な業種のHPに掲載されることを想定【避けていただきたいデザイン】 ・ギラギラした派手すぎるデザイン(金色のグラデーション、過度な装飾など) ・特定の業種にしか合わないデザイン ・文字が小さすぎて読めないデザイン ▼デザイン参考イメージ 以下のようなイメージを参考にしてください ・公的機関の認定マーク(例:QKZ認証、ミルトンシールなど) ・大手メディアの「掲載実績バナー」 ・信頼性を重視した落ち着いたトーンのバナー ※添付バナー画像を参照 ▼納品形式 【必須納品物】 ・3サイズ全てのデザインデータ(PNG形式、背景透過) ・編集可能なデザインデータ(AI、PSD、Figmaなど) ▼報酬・スケジュール ・報酬: ¥30,000円(税込) ・募集期間: 2月2日(月)〜 2月15日(日) ・採用決定: 2月17日(火) |

```html
<!DOCTYPE html>
<html lang="ja">
<head>
<meta charset="utf-8">
<title>達人ディレクトリ掲載専門家 認定バナー</title>
<link rel="stylesheet" href="https://fonts.googleapis.com/css2?family=Noto+Sans+JP:wght@400;500;700;900&display=swap">
<style>
  :root {
    --green: #1d5a2a;
    --green-deep: #174a22;
    --white: #ffffff;
    --seal: #c99a2e;
    --seal-ring: #a87a1c;
    --caption: #333333;
    --page: #ffffff;
  }
  html, body {
    margin: 0;
    width: 1200px;
    height: 1200px;
    overflow: hidden;
    background: var(--page);
    font-family: "Noto Sans JP", sans-serif;
  }
  .canvas { position: relative; width: 1200px; height: 1200px; }

  .banner {
    position: absolute;
    background: var(--green);
    overflow: hidden;
  }
  .caption {
    position: absolute;
    font-size: 17px;
    color: var(--caption);
    letter-spacing: 0.01em;
  }
  .caption small { font-size: 14px; }

  .brand {
    position: absolute;
    display: flex;
    flex-direction: column;
    align-items: center;
    justify-content: center;
    gap: 6px;
    color: var(--white);
    font-weight: 700;
    text-align: center;
    line-height: 1.15;
  }
  .brand-square {
    background: var(--white);
  }

  .seal {
    position: absolute;
    border-radius: 50%;
    background: var(--seal);
    box-shadow: 0 0 0 3px var(--seal-ring) inset;
  }

  .statement {
    position: absolute;
    color: var(--white);
    font-weight: 700;
    line-height: 1.35;
    white-space: nowrap;
  }

  .label-box {
    position: absolute;
    background: var(--white);
    border: 2px solid var(--green-deep);
    display: flex;
    align-items: center;
    justify-content: center;
    color: var(--green);
    font-weight: 500;
    white-space: nowrap;
  }

  /* 320 x 100 */
  .banner--mobile { left: 57px; top: 157px; width: 517px; height: 161px; }
  .banner--mobile .brand { left: 8px; top: 6px; width: 92px; height: 92px; font-size: 15px; }
  .banner--mobile .brand-square { width: 12px; height: 12px; }
  .banner--mobile .statement { left: 112px; top: 14px; font-size: 21px; text-align: center; width: 330px; }
  .banner--mobile .seal { left: 452px; top: 12px; width: 50px; height: 50px; }
  .banner--mobile .label-box { left: 6px; top: 104px; width: 456px; height: 44px; font-size: 31px; }

  /* 300 x 250 */
  .banner--sidebar { left: 618px; top: 157px; width: 522px; height: 435px; }
  .banner--sidebar .brand { left: 186px; top: 22px; width: 150px; height: 170px; font-size: 22px; }
  .banner--sidebar .brand-square { width: 18px; height: 18px; }
  .banner--sidebar .seal { left: 410px; top: 16px; width: 72px; height: 72px; }
  .banner--sidebar .statement { left: 14px; top: 212px; font-size: 30px; }
  .banner--sidebar .label-box { left: 10px; top: 330px; width: 494px; height: 74px; font-size: 33px; }

  /* 728 x 90 */
  .banner--leaderboard { left: 57px; top: 757px; width: 1083px; height: 134px; }
  .banner--leaderboard .brand { left: 16px; top: 12px; width: 100px; height: 110px; font-size: 16px; }
  .banner--leaderboard .brand-square { width: 12px; height: 12px; }
  .banner--leaderboard .statement { left: 138px; top: 14px; font-size: 28px; }
  .banner--leaderboard .seal { left: 1002px; top: 30px; width: 60px; height: 60px; }
  .banner--leaderboard .label-box { left: 132px; top: 74px; width: 840px; height: 48px; font-size: 38px; letter-spacing: 0.12em; }
</style>
</head>
<body>
<main class="canvas">

  <section class="banner banner--mobile" aria-label="320×100 スマートフォン向け横長バナー">
    <div class="brand"><span class="brand-square"></span>達人<br>ディレクトリ</div>
    <p class="statement" style="margin:0">第三者機関に「信頼できる専門家」<br>として認定されました。</p>
    <div class="seal" role="img" aria-label="認定シール"></div>
    <div class="label-box">達人ディレクトリ掲載専門家</div>
  </section>
  <p class="caption" style="left:57px; top:330px; margin:0">320px × 100px<small>(スマートフォン向け横長バナー)</small></p>

  <section class="banner banner--sidebar" aria-label="300×250 サイドバー向け正方形バナー">
    <div class="brand"><span class="brand-square"></span>達人<br>ディレクトリ</div>
    <div class="seal" role="img" aria-label="認定シール"></div>
    <p class="statement" style="margin:0">第三者機関に「信頼できる専門家」<br>として認定されました。</p>
    <div class="label-box">達人ディレクトリ掲載専門家</div>
  </section>
  <p class="caption" style="left:738px; top:614px; margin:0">300px × 250px<small>(サイドバー向け正方形バナー)</small></p>

  <section class="banner banner--leaderboard" aria-label="728×90 PC向けヘッダー/フッター用横長バナー">
    <div class="brand"><span class="brand-square"></span>達人<br>ディレクトリ</div>
    <p class="statement" style="margin:0">第三者機関に「信頼できる専門家」として認定されました。</p>
    <div class="seal" role="img" aria-label="認定シール"></div>
    <div class="label-box">達人ディレクトリ掲載専門家</div>
  </section>
  <p class="caption" style="left:57px; top:905px; margin:0">728px × 90px<small>(PC向けヘッダー/フッター用横長バナー)</small></p>

</main>
</body>
</html>
```